VornaRank.com

We need a new web design for our seo services website at vornarank.com.

Right now we have our homepage, and 2 other pages which we use a html code generator. We need a header and footer and a nice professional looking design to showcase our seo plans.

As for the logo we'll use our company vornaforge.com logo Vorna and change Work to Submit and Technologies to Search Engine Marketing.

We also like to display our textfountain widget and author alert sign up box.

Industry/Entity Type

It Company

Requirements

```html
<!DOCTYPE html>
<html lang="en">
<head>
<meta charset="utf-8">
<title>VornaRank – Internet Marketing &amp; SEO</title>
<link href="https://fonts.googleapis.com/css2?family=Roboto:wght@300;400;500;700&family=Arimo:wght@400;700&display=swap" rel="stylesheet">
<style>
:root{
  --navy:#0b2b7a;
  --navy-dark:#082264;
  --red:#d3141c;
  --text:#333;
  --muted:#777;
  --line:#cfcfcf;
  --panel:#ececec;
  --footer:#3a3a3a;
  --footer-dark:#2a2a2a;
  --gold:#f4b819;
}
*{box-sizing:border-box;margin:0;padding:0}
html,body{width:813px;height:1200px;overflow:hidden;background:#fff}
body{position:relative;font-family:"Arimo",Arial,sans-serif;color:var(--text);font-size:8.5px}
.abs{position:absolute}
.heading{font-family:"Roboto",Arial,sans-serif;font-weight:400}

/* top */
.top-rule{left:0;top:0;width:813px;height:2px;background:var(--red)}
.top-notch{left:429px;top:2px;width:0;height:0;border-left:7px solid transparent;border-right:7px solid transparent;border-top:7px solid var(--red)}
.brand{left:89px;top:30px;display:flex;align-items:center;gap:6px}
.brand-mark{width:12px;height:12px;border-radius:50%;background:var(--red)}
.brand-name{font-family:"Roboto",Arial,sans-serif;font-weight:700;font-size:24px;color:var(--navy);letter-spacing:-.5px;line-height:1}
.brand-sub{left:107px;top:57px;font-family:"Roboto",Arial,sans-serif;font-weight:700;font-size:10px;color:var(--navy)}
.tagline{left:336px;top:27px;width:200px;text-align:center;font-family:"Roboto",Arial,sans-serif;font-size:14px;line-height:17px;color:var(--navy)}
.call{right:92px;top:28px;text-align:right}
.call small{display:block;font-size:8px;color:var(--muted)}
.call strong{display:block;font-family:"Roboto",Arial,sans-serif;font-weight:700;font-size:16px;color:var(--red);margin-top:2px}

/* nav */
.nav{left:0;top:89px;width:813px;height:19px;background:var(--navy)}
.nav ul{position:absolute;left:89px;top:0;display:flex;list-style:none;height:19px}
.nav li{height:19px;line-height:19px;text-align:center;color:#fff;font-size:8.5px;border-right:1px solid #27479a}
.nav li:last-child{border-right:0}
.nav li.active{background:var(--red)}

/* hero */
.hero{left:89px;top:124px;width:428px;height:217px;background:#e9e9e9;padding:5px;box-shadow:0 4px 5px -3px rgba(0,0,0,.25)}
.hero-inner{width:100%;height:100%;background:#fff;position:relative}
.hero-title{left:17px;top:20px;font-size:19px;line-height:19px;color:var(--navy)}
.hero-title span{display:block;color:var(--red);font-size:15.5px}
.hero-globe{left:38px;top:70px;width:152px;height:124px;border-radius:60px 60px 40px 40px;background:radial-gradient(circle at 35% 45%,#4b8fe0 0,#1d5fbf 38%,#e8eef5 40%,#fff 75%)}
.hero-diagram{left:218px;top:30px;width:195px;height:150px;border-radius:50%;background:radial-gradient(circle,#c8ccd2 0,#e1e3e6 45%,#f5f5f5 70%,#fff 72%)}

/* enquiry */
.section-title{font-size:19px;color:var(--navy)}
.section-title em{font-style:normal;color:var(--red)}
.enquiry-title{left:532px;top:119px}
.rule{height:1px;background:var(--line)}
.rule::after{content:"";position:absolute;right:-2px;top:-3px;width:7px;height:7px;border-radius:50%;background:var(--red)}
.field-label{font-size:8.5px;color:var(--text)}
.field{background:#fff;border:1px solid #cacaca;width:147px;height:17px}
.btn-red{background:var(--red);color:#fff;font-size:8.5px;text-align:center;line-height:21px}

/* plans */
.plans-title{left:89px;top:364px;font-size:16px}
.plan{top:403px;width:147px;height:149px;background:#f3f3f3;box-shadow:0 6px 6px -4px rgba(0,0,0,.35)}
.plan-head{height:24px;line-height:24px;text-align:center;font-family:"Roboto",Arial,sans-serif;font-size:13px;color:#222;background:linear-gradient(#d2d2d2,#b9b9b9)}
.plan-head.gold{background:var(--gold)}
.plan-price{height:55px;text-align:center;padding-top:14px;color:var(--navy);font-family:"Roboto",Arial,sans-serif;font-size:12px;border-bottom:1px solid #ddd}
.plan-price .cur{font-size:15px;vertical-align:top;position:relative;top:2px}
.plan-price .amt{font-size:24px;color:var(--red)}
.plan-keys{height:23px;line-height:23px;text-align:center;font-size:8.5px;color:#111;border-bottom:1px solid #ddd}
.quote{position:absolute;left:26px;top:113px;width:95px;height:26px;background:var(--navy);color:#fff;font-weight:700;font-size:8px;line-height:9px;padding:4px 0 0 7px}
.quote svg{position:absolute;right:6px;top:4px}

/* services */
.service-title{font-size:16px;color:var(--navy)}
.service-sub{font-size:10px;color:var(--red);font-family:"Roboto",Arial,sans-serif}
.service-text{width:177px;font-size:8px;line-height:10px;color:#444;text-align:justify}
.btn-navy{background:var(--navy);color:#fff;font-size:8.5px;text-align:center;width:73px;height:20px;line-height:20px}

/* articles */
.articles{left:546px;top:592px;width:175px;height:204px;background:var(--navy);padding:30px 6px 6px}
.articles h3{position:absolute;left:7px;top:8px;font-family:"Roboto",Arial,sans-serif;font-weight:400;font-size:12px;color:#fff}
.articles h3 b{font-weight:700}
.articles-inner{background:#fff;height:166px;padding:9px 9px 0}
.article{font-size:8px;line-height:9.5px;color:#333}
.article h4{font-size:8px;color:var(--navy);margin-bottom:5px;line-height:10px;white-space:nowrap}
.article h4.wrap{white-space:normal}
.article a{display:block;color:var(--red);font-weight:700;margin-top:5px;text-decoration:none}
.article + .article{border-top:1px solid #ccc;margin-top:9px;padding-top:9px}

.alerts{left:546px;top:813px;width:175px;height:185px;background:var(--panel);padding:30px 6px 6px}
.alerts h3{position:absolute;left:11px;top:6px;font-weight:400;font-size:9px;line-height:11px;color:var(--navy)}
.alerts h3 span{color:var(--red)}
.alerts-inner{background:#fff;height:149px;position:relative;font-size:8px;line-height:9.5px;padding:9px 8px}
.alerts-inner a{color:var(--navy)}

/* footer */
.footer{left:0;top:1066px;width:813px;height:114px;background:var(--footer);color:#fff}
.footer h4{position:absolute;top:12px;font-family:"Roboto",Arial,sans-serif;font-weight:300;font-size:13px}
.footer .links{position:absolute;list-style:none;font-size:8px;line-height:15px}
.footer .links li::before{content:"";display:inline-block;width:3px;height:3px;border-radius:50%;background:#fff;margin-right:6px;vertical-align:middle}
.divider{position:absolute;top:16px;width:1px;height:91px;background:#555}
.social{position:absolute;left:392px;list-style:none;font-size:8px}
.social li{display:flex;align-items:center;gap:10px;height:20px}
.social .dot{width:14px;height:14px;border-radius:50%;background:#3c7dc4}
.quote-text{position:absolute;left:564px;top:38px;width:160px;font-size:8px;line-height:10px;color:#eee}
.footer .qmark{position:absolute;font-family:Georgia,serif;font-size:20px;color:#888;line-height:1}
.footer-bar{left:0;top:1180px;width:813px;height:20px;background:var(--footer-dark);color:#fff;font-size:8px;text-align:center;line-height:20px}
</style>
</head>
<body>

<!-- header -->
<div class="abs top-rule"></div>
<div class="abs top-notch"></div>
<div class="abs brand"><span class="brand-mark"></span><span class="brand-name">VornaSubmit</span></div>
<div class="abs brand-sub">Search Engine Marketing</div>
<div class="abs tagline heading">Live Rank Tracking,<br>Reports &amp; Much More</div>
<div class="abs call"><small>Feel Free &amp; Call Us</small><strong>555 014 272</strong></div>

<nav class="abs nav">
  <ul>
    <li class="active" style="width:61px">Home</li>
    <li style="width:76px">Services</li>
    <li style="width:92px">Case Studies</li>
    <li style="width:95px">Pricing Model</li>
    <li style="width:77px">About Us</li>
    <li style="width:90px">Testimonials</li>
    <li style="width:60px">Blog</li>
    <li style="width:81px">Contact Us</li>
  </ul>
</nav>

<!-- hero -->
<section class="abs hero">
  <div class="hero-inner">
    <h1 class="abs hero-title heading">Internet Marketing &amp;<span>Search Engine Optimization</span></h1>
    <div class="abs hero-globe" role="img" aria-label="Globe with a magnifying glass"></div>
    <div class="abs hero-diagram" role="img" aria-label="SEO diagram with coloured bubbles: link building, keywords, reporting, development, research, site analysis"></div>
  </div>
</section>

<!-- enquiry -->
<h2 class="abs section-title heading enquiry-title">Enquiry <em>Now !</em></h2>
<div class="abs rule" style="left:532px;top:150px;width:185px"></div>
<span class="abs field-label" style="left:533px;top:167px">Name :</span>
<div class="abs field" style="left:573px;top:164px"></div>
<span class="abs field-label" style="left:533px;top:197px">Email :</span>
<div class="abs field" style="left:573px;top:193px"></div>
<span class="abs field-label" style="left:533px;top:226px">Phone :</span>
<div class="abs field" style="left:573px;top:222px"></div>
<span class="abs field-label" style="left:533px;top:256px">Details :</span>
<div class="abs field" style="left:573px;top:252px;height:55px"></div>
<div class="abs btn-red" style="left:573px;top:319px;width:67px;height:21px">SUBMIT NOW</div>

<!-- plans -->
<h2 class="abs section-title heading plans-title">Organic <em>SEO Plans</em></h2>
<div class="abs rule" style="left:233px;top:376px;width:484px"></div>

<div class="abs plan" style="left:89px">
  <div class="plan-head">Silver</div>
  <div class="plan-price"><span class="cur">$</span> <span class="amt">500</span> / month</div>
  <div class="plan-keys">Up to <b>10</b> Keywords</div>
  <div class="quote">REQUEST A<br>FREE QOUTE<svg width="19" height="19" viewBox="0 0 19 19"><circle cx="9.5" cy="9.5" r="9.5" fill="#fff"/><path d="M8 5l4.5 4.5L8 14" fill="none" stroke="#0b2b7a" stroke-width="2.4"/></svg></div>
</div>
<div class="abs plan" style="left:251px">
  <div class="plan-head gold">Gold</div>
  <div class="plan-price"><span class="cur">$</span> <span class="amt">750</span> / month</div>
  <div class="plan-keys">Up to <b>20</b> Keywords</div>
  <div class="quote">REQUEST A<br>FREE QOUTE<svg width="19" height="19" viewBox="0 0 19 19"><circle cx="9.5" cy="9.5" r="9.5" fill="#fff"/><path d="M8 5l4.5 4.5L8 14" fill="none" stroke="#0b2b7a" stroke-width="2.4"/></svg></div>
</div>
<div class="abs plan" style="left:412px">
  <div class="plan-head">Platinum</div>
  <div class="plan-price"><span class="cur">$</span><span class="amt">1200</span> / month</div>
  <div class="plan-keys">Up to <b>30</b> Keywords</div>
  <div class="quote">REQUEST A<br>FREE QOUTE<svg width="19" height="19" viewBox="0 0 19 19"><circle cx="9.5" cy="9.5" r="9.5" fill="#fff"/><path d="M8 5l4.5 4.5L8 14" fill="none" stroke="#0b2b7a" stroke-width="2.4"/></svg></div>
</div>
<div class="abs plan" style="left:574px">
  <div class="plan-head">Platinum Plus</div>
  <div class="plan-price"><span class="cur">$</span><span class="amt">1300</span> / month</div>
  <div class="plan-keys">Up to <b>40</b> Keywords</div>
  <div class="quote">REQUEST A<br>FREE QOUTE<svg width="19" height="19" viewBox="0 0 19 19"><circle cx="9.5" cy="9.5" r="9.5" fill="#fff"/><path d="M8 5l4.5 4.5L8 14" fill="none" stroke="#0b2b7a" stroke-width="2.4"/></svg></div>
</div>

<!-- services -->
<h3 class="abs service-title heading" style="left:89px;top:588px">Website Audit</h3>
<div class="abs service-sub" style="left:89px;top:607px">month 1 setup</div>
<div class="abs rule" style="left:89px;top:628px;width:189px"></div>
<p class="abs service-text" style="left:89px;top:639px">Insightful audits that help you understand what work needs to be done and what the website can rank for. Our comprehensive site audit maximizes the effects of our methodology.</p>
<div class="abs btn-navy" style="left:89px;top:702px">VIEW DETAILS</div>

<h3 class="abs service-title heading" style="left:322px;top:588px">Website Optimization</h3>
<div class="abs service-sub" style="left:322px;top:607px">month 1 setup</div>
<div class="abs rule" style="left:322px;top:628px;width:189px"></div>
<p class="abs service-text" style="left:322px;top:639px">Starting with your website, we will optimize all key aspects of its targeted pages. Our optimization process ensures your website will be ready to rank once we begin our off-page marketing efforts.</p>
<div class="abs btn-navy" style="left:322px;top:702px">VIEW DETAILS</div>

<h3 class="abs service-title heading" style="left:89px;top:744px">Rich Searchly Listing</h3>
<div class="abs service-sub" style="left:89px;top:763px">month 1 setup</div>
<div class="abs rule" style="left:89px;top:788px;width:189px"></div>
<p class="abs service-text" style="left:89px;top:799px">We'll advise you on how to get the best listing you can in the search results pages. These types of listings get more clicks because of the dynamic information.</p>
<div class="abs btn-navy" style="left:89px;top:861px">VIEW DETAILS</div>

<h3 class="abs service-title heading" style="left:322px;top:744px">Citation &amp; Link Building</h3>
<div class="abs service-sub" style="left:322px;top:763px">month 1 setup</div>
<div class="abs rule" style="left:322px;top:789px;width:189px"></div>
<p class="abs service-text" style="left:322px;top:802px">Starting with your website, we will optimize all key aspects of its targeted pages. Our optimization process ensures your website will be ready to rank once we begin our off-page marketing efforts.</p>
<div class="abs btn-navy" style="left:322px;top:861px">VIEW DETAILS</div>

<h3 class="abs service-title heading" style="left:89px;top:905px">Content Marketting</h3>
<div class="abs service-sub" style="left:89px;top:924px">ongoing monthly campaign</div>
<div class="abs rule" style="left:89px;top:949px;width:189px"></div>
<p class="abs service-text" style="left:89px;top:960px">We'll start getting the word out about your business quickly. In Month 1 we do things like Press Releases, Magazine Features, and Social Sharing.</p>
<div class="abs btn-navy" style="left:89px;top:1018px">VIEW DETAILS</div>

<h3 class="abs service-title heading" style="left:322px;top:905px">Reporting &amp; Strategy</h3>
<div class="abs service-sub" style="left:322px;top:924px">monthly</div>
<div class="abs rule" style="left:322px;top:950px;width:189px"></div>
<p class="abs service-text" style="left:322px;top:962px">Our live dashboard always has up to date traffic information and search results rankings. You can log in at any time, or get a comprehensive PDF report showing rankings and traffic.</p>
<div class="abs btn-navy" style="left:322px;top:1018px">VIEW DETAILS</div>

<!-- sidebar -->
<aside class="abs articles">
  <h3>Articles by <b>Dana Holt</b></h3>
  <div class="articles-inner">
    <div class="article">
      <h4>Different Kinds of Internet Marketing</h4>
      Internet marketing is a very diverse and growing and field. There are many different paths ...
      <a href="#">continue</a>
    </div>
    <div class="article">
      <h4 class="wrap">Seven Ways to Promote Your<br>New Website</h4>
      Thousands of web pages are being added to the Internet daily. If you want your ...
      <a href="#">continue</a>
    </div>
  </div>
</aside>

<aside class="abs alerts">
  <h3>Dana Holt's Expert Author<br><span>Email Alerts</span></h3>
  <div class="alerts-inner">
    <p>Sign up to receive email alerts of<br><b>Dana Holt's</b> latest articles from<br><a href="#">TextFountain.com!</a></p>
    <span class="abs field-label" style="left:9px;top:58px">Name :</span>
    <div class="abs field" style="left:44px;top:54px;width:115px"></div>
    <span class="abs field-label" style="left:9px;top:87px">Email :</span>
    <div class="abs field" style="left:44px;top:83px;width:115px"></div>
    <div class="abs btn-navy" style="left:44px;top:115px;width:51px;height:18px;line-height:18px">SIGNUP</div>
  </div>
</aside>

<!-- footer -->
<footer class="abs footer">
  <h4 style="left:89px">Quick Links</h4>
  <ul class="links" style="left:89px;top:38px"><li>Services</li><li>Case Studies</li><li>Pricing Model</li></ul>
  <span class="divider" style="left:206px"></span>
  <ul class="links" style="left:239px;top:38px"><li>About Us</li><li>Testimonials</li><li>Blog</li><li>Contact Us</li></ul>
  <span class="divider" style="left:345px"></span>
  <h4 style="left:392px">Follow Us</h4>
  <ul class="social" style="top:38px">
    <li><span class="dot"></span>Circlebook</li>
    <li><span class="dot"></span>Chirper</li>
    <li><span class="dot"></span>Workweb</li>
  </ul>
  <span class="divider" style="left:505px"></span>
  <h4 style="left:544px">Testimonials</h4>
  <span class="qmark" style="left:545px;top:36px">&ldquo;</span>
  <p class="quote-text">Lorem ipsum dolor sit amet, consectetur adipisicing elit, sed do eiusmod tempor incididunt ut labore et dolore magna aliqua ...</p>
  <span class="qmark" style="left:711px;top:60px">&rdquo;</span>
  <p class="abs" style="left:546px;top:80px;font-size:8px;color:#ddd"><b style="color:#fff">John,</b> 18/09/13</p>
  <p class="abs" style="left:700px;top:96px;font-size:8px;font-weight:700;text-decoration:underline">more</p>
</footer>
<div class="abs footer-bar">Copyright © 2013 <b>VornaSubmit Internet Marketing Service</b>. All rights reserved.</div>

</body>
</html>
```